New startup requiring business card

New company needed a business card / logo. Company name is
Minthel
Company is providing IT software sales, partnering and consulting services across the APAC region. Catch line is "Linked for Progress".
We currently have a feeling yellow as the primary colour given its meaning across the region but open to ideas. Main brief is we want something smart, clean and professional while still leveraging the strength of the name.
A major part of the business is mutually beneficial partnerships, not sure if this helps but maybe visual around linkages between objects.
Also wanting a standard size card, preference is something that will have a D/S cello sheen finish in a matt. But again open to ideas, wow us!
Software

```html
<!DOCTYPE html>
<html lang="en">
<head>
<meta charset="utf-8">
<title>Minthel Business Card</title>
<link rel="stylesheet" href="https://fonts.googleapis.com/css2?family=Cabin:wght@400;500;600&display=swap">
<style>
  :root {
    --backdrop: #ececec;
    --card: #fbfbf9;
    --ink: #2a2a2a;
    --muted: #6b6b6b;
    --coral: #f2745a;
    --shadow: rgba(0, 0, 0, 0.12);
  }
  * { box-sizing: border-box; margin: 0; padding: 0; }
  html, body {
    width: 1200px;
    height: 861px;
    overflow: hidden;
    background: var(--backdrop);
    font-family: "Cabin", "Gill Sans", sans-serif;
  }
  .stage {
    position: relative;
    width: 1200px;
    height: 861px;
  }
  .card {
    position: absolute;
    top: 293px;
    width: 490px;
    height: 280px;
    background: var(--card);
    box-shadow: 0 10px 30px var(--shadow);
  }
  .card--front { left: 85px; }
  .card--back { left: 625px; }

  .brand {
    position: absolute;
    left: 0;
    right: 0;
    top: 98px;
    display: flex;
    flex-direction: column;
    align-items: center;
    text-align: center;
  }
  .brand__name {
    font-size: 48px;
    font-weight: 500;
    line-height: 1;
    color: var(--ink);
  }
  .brand__tagline {
    margin-top: 12px;
    font-size: 14px;
    font-weight: 400;
    letter-spacing: 1.5px;
    color: var(--muted);
  }

  .person {
    position: absolute;
    left: 80px;
    top: 92px;
    font-size: 32px;
    font-weight: 500;
    line-height: 1;
    color: var(--coral);
  }
  .person__first, .person__last { display: block; }
  .person__last { margin-left: -20px; }
  .contact {
    position: absolute;
    left: 222px;
    top: 104px;
    list-style: none;
    font-size: 13px;
    line-height: 1.75;
    letter-spacing: 0.4px;
    color: var(--coral);
  }
</style>
</head>
<body>
<main class="stage">
  <section class="card card--front" aria-label="Card front">
    <div class="brand">
      <span class="brand__name">Minthel</span>
      <span class="brand__tagline">Linked for progress</span>
    </div>
  </section>

  <section class="card card--back" aria-label="Card back">
    <h1 class="person">
      <span class="person__first">Dorian</span>
      <span class="person__last">Vell</span>
    </h1>
    <ul class="contact">
      <li>(914) 555-0187</li>
      <li>hello@minthel.com</li>
      <li>minthel.com</li>
    </ul>
  </section>
</main>
</body>
</html>
```